Bright Meadow Party Coaches is excited to bring you Fenwick Valley’s Prime luxury limousine ser...

Leisure TransportationWedding DayWe will make your wedding day special and one to remember. Bright Meadow Party Coaches offers custom wedding transportation packages that are designed around your every need. Call our transportation consultant and learn how we can help you have a stress free and perfectly planned wedding event.PromsWe put safety first and give you piece of mind when we transport your loved ones.Special Occasions Bright Meadow Party Coaches professional chauffeured services will make any special event extraordinary. You will feel safe while our professional chauffeurs drive you in style and luxury.Corporate EventsNorth Coast Event Charters is a leader in professional chauffeured transportation services. Our highly trained staff will take the stress out of getting you to and from your destination. Bright Meadow Party Coaches is dedicated to the highest quality of services. Our top-of-the-line Calder-Voss Tramway is always safety inspected and cleaned before each use. Tours From the ocean to the redwoods, we offer tours to suit your needs.,Airport Service We are business ground travel experts. Our doo-to-door limousine can accommodate up to 10 passengers, and service all private and public airports

Target Market(s)

These brochures are going in motels and restaurants.

Font styles to use
Script

Colors
fed55c

Requirements
Must have
• Gold and black are the business colors. Check brand identity PDF

```html
<!DOCTYPE html>
<html lang="en">
<head>
<meta charset="utf-8">
<title>Bright Meadow Party Coaches – Trifold Brochure</title>
<link href="https://fonts.googleapis.com/css2?family=Marcellus&family=Open+Sans:wght@400;600;700&family=Great+Vibes&display=swap" rel="stylesheet">
<style>
:root{
  --gold:#c29c46;
  --gold-light:#d9b964;
  --black:#121212;
  --charcoal:#2b2b2b;
  --grey:#5a5a5a;
  --paper:#ffffff;
  --ink:#2a2a2a;
  --bg:#e4e4e4;
}
*{box-sizing:border-box;margin:0;padding:0}
html,body{width:1200px;height:2400px;overflow:hidden;background:var(--bg)}
body{position:relative;font-family:"Open Sans",Arial,sans-serif;color:var(--ink)}
.spread{position:absolute;left:60px;width:1080px;height:834px;display:flex;box-shadow:0 12px 30px rgba(0,0,0,.25)}
.spread--outside{top:220px}
.spread--inside{top:1330px}
.panel{position:relative;width:360px;height:834px;overflow:hidden}
.panel svg.shapes{position:absolute;inset:0}
.layer{position:absolute;left:0;right:0}
.heading{font-family:"Marcellus",Georgia,serif;color:var(--gold);letter-spacing:.04em;text-transform:uppercase}
.script{font-family:"Great Vibes",cursive;}
.body-text{font-size:10.5px;line-height:1.55}
.btn{display:inline-block;border:1.5px solid var(--gold);border-radius:14px;padding:4px 16px;font-size:10px;font-weight:600;letter-spacing:.08em;text-transform:uppercase}
.site{font-family:"Open Sans",sans-serif;font-weight:700;font-size:15px;letter-spacing:.05em;text-align:center}
.brand-name{font-family:"Open Sans",sans-serif;font-weight:600;font-size:11px;letter-spacing:.1em;text-transform:uppercase;color:#fff;text-align:center;line-height:1.3}

/* flap */
.panel--flap{background:linear-gradient(180deg,var(--charcoal),var(--black))}
.flap-copy{top:300px;padding:0 30px;color:#ddd}
.flap-copy .heading{font-size:16px;margin-bottom:10px}
.flap-copy ul{list-style:none;margin:10px 0 16px}
.flap-copy li{font-size:10.5px;line-height:1.7;padding-left:12px;position:relative}
.flap-copy li::before{content:"";position:absolute;left:0;top:7px;width:5px;height:5px;border-radius:50%;background:var(--gold)}
.flap-copy .btn{color:var(--gold)}
.flap-site{bottom:12px;color:var(--black)}

/* back */
.panel--back{background:var(--gold)}
.back-copy{top:260px;padding:0 34px;text-align:center;color:var(--black)}
.back-copy .heading{font-size:22px;color:var(--black)}
.back-copy .script{font-size:26px;color:#fff;margin:2px 0 14px}
.back-copy .body-text{font-size:11.5px;margin-bottom:12px}
.back-copy .btn{border-color:var(--black);color:var(--black);margin:6px 0 12px}
.back-contact{font-size:11px;line-height:1.6}
.back-phone{bottom:16px;text-align:center;color:#fff;font-weight:600;font-size:16px;letter-spacing:.1em}

/* cover */
.panel--cover{background:var(--black)}
.cover-title{top:628px;text-align:center}
.cover-title .heading{font-size:25px}
.cover-title .script{font-size:25px;color:#fff}
.cover-site{bottom:16px;color:var(--black)}

/* inside left */
.panel--intro{background:var(--paper)}
.intro-copy{top:38px;padding:0 30px}
.intro-copy .heading{font-size:19px;margin-bottom:12px}
.intro-copy .body-text{margin-bottom:10px;color:var(--ink)}

/* services */
.panel--services{background:var(--gold)}
.services-title{top:40px;text-align:center;color:#fff;font-family:"Marcellus",serif;font-size:17px;letter-spacing:.12em}
.services-grid{top:110px;padding:0 26px;display:grid;grid-template-columns:repeat(3,1fr);row-gap:16px}
.service{text-align:center;font-size:10px;font-weight:600;color:var(--black)}
.service-dot{width:62px;height:62px;margin:0 auto 6px;border-radius:50%;border:2px solid var(--black);background:rgba(255,255,255,.12);display:flex;align-items:center;justify-content:center}
.service-dot svg{width:30px;height:30px}
.services-tag{top:540px;text-align:center;padding:0 24px}
.services-tag .script{font-size:23px;color:#fff;line-height:1.1}
.services-tag p.body-text{font-size:10px;margin-top:6px;color:var(--black)}

/* features */
.panel--features{background:var(--black)}
.features-copy{top:330px;padding:0 30px;color:#ddd}
.features-copy .script{font-size:24px;color:var(--gold);margin:6px 0 4px}
.pricing{top:660px;text-align:center;color:#fff}
.pricing .heading{font-size:18px;margin-bottom:8px}
.pricing p{font-size:10.5px;line-height:1.6}
</style>
</head>
<body>

<section class="spread spread--outside">
  <article class="panel panel--flap">
    <svg class="shapes" viewBox="0 0 360 834">
      <defs><linearGradient id="forest" x1="0" y1="0" x2="0" y2="1"><stop offset="0" stop-color="#3f5a2e"/><stop offset="1" stop-color="#6b6a5c"/></linearGradient>
      <linearGradient id="pinkish" x1="0" y1="0" x2="1" y2="1"><stop offset="0" stop-color="#c9a58f"/><stop offset="1" stop-color="#3a2a24"/></linearGradient></defs>
      <path d="M0 0H360V200Q180 270 0 230Z" fill="url(#forest)" role="img" aria-label="Coach driving on a road through tall redwood trees"/>
      <path d="M0 236Q180 276 360 206" fill="none" stroke="#c29c46" stroke-width="3"/>
      <circle cx="296" cy="252" r="40" fill="url(#pinkish)" stroke="#c29c46" stroke-width="3" role="img" aria-label="Guests enjoying an evening out"/>
      <path d="M0 800Q180 770 360 790V834H0Z" fill="#c29c46"/>
    </svg>
    <div class="layer flap-copy">
      <h2 class="heading">Bright Meadow Party Coaches</h2>
      <p class="body-text">Bright Meadow Party Coaches is excited to bring you Fenwick Valley’s Prime luxury limousine service. Our chauffeurs will make any special event extraordinary.</p>
      <ul>
        <li>Up to 10 passengers in comfort</li>
        <li>Premium sound and LED lighting</li>
        <li>Leather seating throughout</li>
        <li>Safety inspected before each use</li>
        <li>Professional, courteous chauffeurs</li>
        <li>Door-to-door airport service</li>
        <li>Every ride is tailored to your needs</li>
      </ul>
      <span class="btn">Book your event today</span>
    </div>
    <p class="layer site flap-site">www.brightmeadowcoaches.com</p>
  </article>

  <article class="panel panel--back">
    <svg class="shapes" viewBox="0 0 360 834">
      <path d="M0 0H360V150Q180 240 0 150Z" fill="#121212"/>
      <path d="M0 158Q180 248 360 158" fill="none" stroke="#fff" stroke-width="2"/>
      <circle cx="180" cy="150" r="64" fill="#5a5a5a" stroke="#c29c46" stroke-width="3"/>
      <path d="M0 800Q180 770 360 800V834H0Z" fill="#121212"/>
    </svg>
    <div class="layer brand-name" style="top:135px">Bright Meadow<br>Party Coaches</div>
    <div class="layer back-copy">
      <h2 class="heading">Luxury Transportation</h2>
      <p class="script">Bright Meadow Party Coaches</p>
      <p class="body-text">We put safety first and give you piece of mind when we transport your loved ones.</p>
      <p class="body-text">Call our transportation consultant and learn how we can help you have a stress free and perfectly planned wedding event.</p>
      <span class="btn">Book your event today</span>
      <p class="back-contact">555.014.2290<br>hello@brightmeadowcoaches.com<br>www.brightmeadowcoaches.com</p>
    </div>
    <p class="layer back-phone">555.014.2290</p>
  </article>

  <article class="panel panel--cover">
    <svg class="shapes" viewBox="0 0 360 834">
      <defs><linearGradient id="sky" x1="0" y1="0" x2="0" y2="1"><stop offset="0" stop-color="#8fb0d6"/><stop offset=".45" stop-color="#cfd8e2"/><stop offset=".7" stop-color="#55575b"/><stop offset="1" stop-color="#8a3a34"/></linearGradient></defs>
      <path d="M0 50Q180 -10 360 50V470Q180 560 0 470Z" fill="url(#sky)" role="img" aria-label="Open coach door with red carpet and gold stanchions"/>
      <path d="M0 482Q180 572 360 482" fill="none" stroke="#c29c46" stroke-width="4"/>
      <circle cx="180" cy="530" r="64" fill="#5a5a5a" stroke="#c29c46" stroke-width="3"/>
      <path d="M0 790Q180 760 360 780V834H0Z" fill="#c29c46"/>
    </svg>
    <div class="layer brand-name" style="top:515px">Bright Meadow<br>Party Coaches</div>
    <div class="layer cover-title">
      <h1 class="heading">Luxury Transportation</h1>
      <p class="script">for some of life’s biggest moments</p>
    </div>
    <p class="layer site cover-site">www.brightmeadowcoaches.com</p>
  </article>
</section>

<section class="spread spread--inside">
  <article class="panel panel--intro">
    <svg class="shapes" viewBox="0 0 360 834">
      <defs><linearGradient id="coach" x1="0" y1="0" x2="1" y2="0"><stop offset="0" stop-color="#1d1d1f"/><stop offset=".6" stop-color="#3b3b40"/><stop offset="1" stop-color="#9a9ea4"/></linearGradient></defs>
      <path d="M0 560Q180 540 360 560V760Q180 790 0 760Z" fill="url(#coach)" role="img" aria-label="Black coach with open door and red carpet"/>
      <path d="M0 764Q180 796 360 764V790Q180 820 0 790Z" fill="#c29c46"/>
      <path d="M0 792Q180 822 360 792V834H0Z" fill="#121212"/>
    </svg>
    <div class="layer intro-copy">
      <h2 class="heading">Luxury Transportation</h2>
      <p class="body-text">Fenwick Valley is all about fun, and there’s no better way to travel this exciting community than in one of our luxurious Calder-Voss Tramway coaches. Come take a ride in our twelve-passenger limousine with leather seating, LED lighting, a premium sound system, and a fully stocked bar.</p>
      <p class="body-text">Whether it’s a special night on the town, prom, wedding, or corporate event, Bright Meadow Party Coaches gives you the experience and service you expect from luxury limousine travel.</p>
      <p class="body-text">Every ride is tailored to your personal needs, and you never have to worry about parking or how to find your destination. Your personal chauffeur has everything covered. Just hop in, sit back, relax with a drink and enjoy the experience.</p>
      <p class="body-text">You’ll be whisked off to your destination and taken to the front door with no worries about parking. With Bright Meadow Party Coaches, you’ll always arrive in style.</p>
    </div>
  </article>

  <article class="panel panel--services">
    <svg class="shapes" viewBox="0 0 360 834">
      <defs><linearGradient id="party" x1="0" y1="0" x2="1" y2="1"><stop offset="0" stop-color="#6b3fa0"/><stop offset="1" stop-color="#1a1a2a"/></linearGradient></defs>
      <path d="M0 0H360V70Q180 110 0 70Z" fill="#121212"/>
      <circle cx="110" cy="730" r="46" fill="url(#party)" stroke="#121212" stroke-width="3" role="img" aria-label="Coach interior with purple lighting"/>
      <circle cx="250" cy="730" r="46" fill="url(#party)" stroke="#121212" stroke-width="3" role="img" aria-label="Lounge seating inside the coach"/>
    </svg>
    <h2 class="layer services-title">OUR SERVICES</h2>
    <div class="layer services-grid">
      <div class="service"><div class="service-dot"><svg viewBox="0 0 30 30"><path d="M3 17L27 12M15 14L10 5M15 15L12 25" stroke="#121212" stroke-width="2.5" fill="none" stroke-linecap="round"/></svg></div>Airport Service</div>
      <div class="service"><div class="service-dot"><svg viewBox="0 0 30 30"><rect x="3" y="10" width="24" height="10" rx="2" fill="#121212"/><circle cx="9" cy="22" r="3" fill="#121212"/><circle cx="21" cy="22" r="3" fill="#121212"/></svg></div>Travel Service</div>
      <div class="service"><div class="service-dot"><svg viewBox="0 0 30 30"><path d="M8 5L22 5L15 15Z M15 15V25M10 25H20" stroke="#121212" stroke-width="2.5" fill="none"/></svg></div>Celebrations</div>
      <div class="service"><div class="service-dot"><svg viewBox="0 0 30 30"><circle cx="15" cy="18" r="8" stroke="#121212" stroke-width="2.5" fill="none"/><path d="M12 6H18L15 10Z" fill="#121212"/></svg></div>Engagement</div>
      <div class="service"><div class="service-dot"><svg viewBox="0 0 30 30"><path d="M15 4L18 12L26 12L20 17L22 25L15 20L8 25L10 17L4 12L12 12Z" fill="#121212"/></svg></div>Prom Events</div>
      <div class="service"><div class="service-dot"><svg viewBox="0 0 30 30"><rect x="5" y="14" width="20" height="11" fill="#121212"/><path d="M10 14V8M15 14V8M20 14V8" stroke="#121212" stroke-width="2"/></svg></div>Birthday Parties</div>
      <div class="service"><div class="service-dot"><svg viewBox="0 0 30 30"><circle cx="11" cy="17" r="6" stroke="#121212" stroke-width="2.5" fill="none"/><circle cx="19" cy="17" r="6" stroke="#121212" stroke-width="2.5" fill="none"/></svg></div>Weddings</div>
      <div class="service"><div class="service-dot"><svg viewBox="0 0 30 30"><path d="M9 5H21V14Q21 20 15 20Q9 20 9 14Z M15 20V25M10 25H20" stroke="#121212" stroke-width="2.5" fill="none"/></svg></div>Bar Crawls</div>
      <div class="service"><div class="service-dot"><svg viewBox="0 0 30 30"><path d="M8 6H22L15 16Z M15 16V25M10 25H20" stroke="#121212" stroke-width="2.5" fill="none"/><circle cx="21" cy="9" r="2" fill="#121212"/></svg></div>Bachelor Parties</div>
    </div>
    <div class="layer services-tag">
      <p class="script">Just hop in, sit back, relax with a drink<br>and enjoy the ride.</p>
      <p class="body-text">With Bright Meadow Party Coaches,<br>you’ll always arrive in style.</p>
    </div>
  </article>

  <article class="panel panel--features">
    <svg class="shapes" viewBox="0 0 360 834">
      <defs><linearGradient id="lounge" x1="0" y1="0" x2="1" y2="1"><stop offset="0" stop-color="#c7b07a"/><stop offset=".5" stop-color="#4b2f5e"/><stop offset="1" stop-color="#161616"/></linearGradient></defs>
      <path d="M0 0H360V260Q180 330 0 290Z" fill="url(#lounge)" role="img" aria-label="Passengers toasting inside the lit coach"/>
      <path d="M0 296Q180 336 360 266" fill="none" stroke="#c29c46" stroke-width="3"/>
      <path d="M0 640Q180 600 360 610" fill="none" stroke="#c29c46" stroke-width="4"/>
      <path d="M0 648Q180 608 360 618V834H0Z" fill="#1e1e1e"/>
    </svg>
    <div class="layer features-copy">
      <p class="script">Your Red-Carpet Experience</p>
      <p class="body-text">Bright Meadow Party Coaches provides luxury transportation for small or large groups. Our chauffeurs roll out the red carpet and make every guest feel like a star from pickup to drop-off.</p>
      <p class="script">Upscale Luxury Features</p>
      <p class="body-text">Our top-of-the-line Calder-Voss Tramway offers leather seating, LED mood lighting, a premium sound system, and a fully stocked bar. It is always safety inspected and cleaned before each use.</p>
    </div>
    <div class="layer pricing">
      <h2 class="heading">Pricing &amp; Packages</h2>
      <p>HOURLY RATE: $100 – 4 hour min.</p>
      <p>PROMS: $500 – 6 hours</p>
      <p>VIP: $700 – 8 hours</p>
      <p>WEDDING: $1,500 – 10 hours</p>
      <p>Custom packages available</p>
    </div>
  </article>
</section>

</body>
</html>
```